Auto Mechanic business card

Need a general business card for GearWrenchPro.
Name on card should be 'Roving Wrench'
Tel # (869) 412 3096
Address is - Fern Lane, Basseterre, St. Kitts
Whatsapp and facebook symbols should be added
On back of card should include services offered
General Repairs
Brakes
Tune Ups
Suspensions
Oil Leaks
Dent repairs
Suspensions
Car Sales
Tyre Repairs
General service
Check Engine Light
Minor Electricals

Target Market(s)

General Population, University students

Industry/Entity Type

Auto Mechanic

Contact Information for Business Card

Roving Wrench

Requirements
Must have
• 2 Sides

```html
<!DOCTYPE html>
<html lang="en">
<head>
<meta charset="utf-8">
<title>Roving Wrench – Business Card</title>
<link href="https://fonts.googleapis.com/css2?family=Montserrat:wght@500;700;800&family=Exo+2:ital,wght@1,800&display=swap" rel="stylesheet">
<style>
  :root {
    --backdrop: #000000;
    --card-red: #d51016;
    --deep-red: #b80f14;
    --shadow-red: #6e070b;
    --navy: #142f8a;
    --white: #ffffff;
  }
  * { margin: 0; padding: 0; box-sizing: border-box; }
  html, body { width: 1200px; height: 1200px; overflow: hidden; background: var(--backdrop); }
  .canvas { position: relative; width: 1200px; height: 1200px; }

  .card {
    position: absolute;
    width: 693px;
    height: 396px;
    background: var(--card-red);
    overflow: hidden;
    font-family: "Montserrat", sans-serif;
    color: var(--white);
  }
  .card-front { left: 157px; top: 181px; display: flex; align-items: center; justify-content: center; }
  .card-back { left: 304px; top: 601px; }

  .front-name {
    font-weight: 800;
    font-size: 54px;
    letter-spacing: 1px;
    text-transform: uppercase;
    color: var(--white);
  }

  .decor-wrench {
    position: absolute; left: 466px; top: 10px; width: 240px; height: 76px;
    background: var(--deep-red); border-radius: 38px 0 0 38px;
  }
  .decor-gear {
    position: absolute; left: -50px; top: 250px; width: 224px; height: 224px;
    background: var(--deep-red); border-radius: 50%;
  }

  .repairs-banner { position: absolute; left: 0; top: 0; width: 460px; height: 100px; }
  .repairs-title {
    position: absolute; left: 28px; top: 28px;
    font-family: "Exo 2", sans-serif; font-style: italic; font-weight: 800;
    font-size: 32px; letter-spacing: 1px; color: var(--navy);
  }

  .service-list {
    position: absolute; left: 0; top: 105px; width: 693px;
    list-style: none; text-align: center;
    font-weight: 500; font-size: 23px; line-height: 30.8px; letter-spacing: 0.6px;
  }
  .service-list li { white-space: nowrap; }
  .service-list span::before {
    content: ""; display: inline-block; width: 7px; height: 7px;
    background: var(--white); margin: 0 6px 4px 8px; vertical-align: middle;
  }

  .phone-band { position: absolute; left: 250px; top: 262px; width: 443px; height: 110px; }
  .phone-number {
    position: absolute; left: 343px; top: 300px;
    font-family: "Exo 2", sans-serif; font-style: italic; font-weight: 800;
    font-size: 37px; color: var(--navy); letter-spacing: 0.5px;
  }

  .social { position: absolute; left: 28px; top: 321px; display: flex; align-items: center; gap: 10px; }
  .social-dot { width: 66px; height: 66px; border-radius: 50%; background: var(--white); }
  .social-name { font-weight: 700; font-size: 15px; color: var(--white); }

  .address {
    position: absolute; right: 36px; top: 370px;
    font-weight: 500; font-size: 18px; letter-spacing: 0.4px;
  }
</style>
</head>
<body>
<main class="canvas">

  <section class="card card-front" aria-label="Card front">
    <h1 class="front-name">Roving Wrench</h1>
  </section>

  <section class="card card-back" aria-label="Card back">
    <div class="decor-wrench" role="img" aria-label="Faint wrench decoration"></div>
    <div class="decor-gear" role="img" aria-label="Faint gear decoration"></div>

    <svg class="repairs-banner" viewBox="0 0 460 100" aria-hidden="true">
      <polygon points="0,60 441,17 379,88 0,88" fill="var(--shadow-red)"/>
      <polygon points="0,17 441,17 379,75 0,75" fill="var(--white)"/>
    </svg>
    <h2 class="repairs-title">GENERAL REPAIRS</h2>

    <ul class="service-list">
      <li><span>BRAKES</span> &nbsp;<span>TUNE UPS</span></li>
      <li><span>SUSPENSIONS</span><span>OIL LEAKS</span><span>DENT REPAIRS</span></li>
      <li><span>CAR SALES</span><span>TYRE REPAIR</span></li>
      <li><span>GENERAL SERVICE</span><span>CHECK ENGINE LIGHT</span></li>
      <li><span>MINOR ELECTRICALS</span></li>
    </ul>

    <svg class="phone-band" viewBox="0 0 443 110" aria-hidden="true">
      <polygon points="49,87 443,87 443,101 75,101" fill="var(--shadow-red)"/>
      <rect x="73" y="31" width="370" height="56" fill="var(--white)"/>
      <circle cx="41" cy="47" r="38" fill="var(--white)" stroke="var(--navy)" stroke-width="6"/>
      <path d="M28 33 c-4 4 -3 12 4 21 c7 9 15 13 20 10 l3 -3 c1 -1 1 -3 0 -4 l-6 -5 c-1 -1 -3 -1 -4 0 l-3 2 c-3 -1 -8 -7 -9 -10 l2 -3 c1 -1 1 -3 0 -4 l-4 -6 c-1 -1 -3 -1 -4 0 z" fill="var(--navy)"/>
    </svg>
    <p class="phone-number">(869) 412 3096</p>

    <div class="social">
      <span class="social-dot" aria-hidden="true"></span>
      <span class="social-name">Roving Wrench</span>
    </div>

    <p class="address">Fern Lane, Basseterre, St. Kitts</p>
  </section>

</main>
</body>
</html>
```